Gewinnspielseite
Zielgruppe
Zielgruppe sind halt Gewinnspieler und Schnäppchenjäger
Aufgabenstellung
Es soll ein Design für eine Gewinnspielseite erstellt werden. Ich benötige eine Main-Seite die ruhig grafisch schön ist und dann eine Unterseite wo ich entsprechend Inhalte einspielen kann. Typische Gewinnspielseiten von uns unter www.kronmuehle.de wo die Unterseiten Contents dann auch gezeigt werden. Menüpunkte: Datenschutz, Teilnahmebedingungen, Impressum, Preis, Startseite

```html
<!DOCTYPE html>
<html lang="de">
<head>
<meta charset="utf-8">
<title>Gewinnspiel – LCD-Fernseher gewinnen</title>
<link rel="stylesheet" href="https://fonts.googleapis.com/css2?family=Exo+2:ital,wght@0,700;1,700;1,800;1,900&family=Open+Sans:wght@400;600&display=swap">
<style>
:root{
  --page-bg:#0a2a0c;
  --page-edge:#0e3a10;
  --column-bg:#000;
  --headline-blue:#6ab8ef;
  --info-blue:#4aa3e0;
  --accent-green:#2fbf3a;
  --rule-green:#1f8a22;
  --text-light:#e8e8e8;
  --text-muted:#b5b5b5;
  --footer-link:#2aa535;
}
*{box-sizing:border-box;margin:0;padding:0}
html,body{width:1200px;height:900px;overflow:hidden}
body{background:linear-gradient(90deg,var(--page-edge),var(--page-bg) 10%,var(--page-bg) 90%,var(--page-edge));font-family:"Open Sans",Verdana,sans-serif;position:relative}
.column{position:absolute;left:132px;top:0;width:936px;height:900px;background:var(--column-bg);border-top:6px solid #1c4f8a;border-bottom:9px solid #1d7a20;overflow:hidden}
.abs{position:absolute}
.hero{left:0;top:0;width:936px;height:384px}
.hero-photo{left:70px;top:9px;width:355px;height:357px;border-radius:6px;background:linear-gradient(160deg,#2a2a2a,#050505 60%,#1a1a1a);box-shadow:0 0 40px rgba(40,160,60,.35)}
.headline{right:48px;top:22px;text-align:right;font-family:"Exo 2",sans-serif;font-style:italic;font-weight:900;color:var(--headline-blue);text-transform:uppercase;letter-spacing:2px;line-height:1;text-shadow:0 0 10px rgba(80,160,230,.6);white-space:nowrap}
.headline span{display:block;font-size:42px;margin-top:2px}
.headline .small{font-size:30px;margin-right:38px}
.headline .l2{margin-right:128px}
.headline .l3{margin-right:30px}
.headline .l4{margin-right:0}
.pill{display:flex;align-items:center;justify-content:center;font-family:"Exo 2",sans-serif;font-weight:700;color:#fff;letter-spacing:1px;white-space:nowrap;background:linear-gradient(#6fb2ea,#2c73b8 55%,#1c5a99);border-radius:20px 4px 4px 20px;clip-path:polygon(0 0,92% 0,100% 50%,92% 100%,0 100%)}
.hero-button{left:651px;top:279px;width:263px;height:45px;font-size:22px}
.section-title{font-family:"Exo 2",sans-serif;font-style:italic;font-weight:700;font-size:17px;letter-spacing:1.5px;color:var(--text-light);text-transform:uppercase;border-bottom:2px solid var(--rule-green);padding-bottom:4px;white-space:nowrap}
.section-title em{color:var(--accent-green)}
.prize-photo{left:40px;top:502px;width:170px;height:116px;border-radius:4px;background:linear-gradient(150deg,#3a3a3a,#060606 55%,#202020);box-shadow:0 0 14px rgba(40,170,60,.5)}
.prize-facts{left:248px;top:498px;font-family:"Exo 2",sans-serif;font-weight:700;font-size:16px;line-height:20px;color:var(--info-blue);letter-spacing:1px;text-transform:uppercase;white-space:nowrap}
.prize-call{left:248px;top:590px;font-family:"Exo 2",sans-serif;font-weight:700;font-size:16px;line-height:20px;color:var(--accent-green);letter-spacing:1px;text-transform:uppercase;white-space:nowrap}
.form-label{left:475px;font-family:"Exo 2",sans-serif;font-weight:700;font-size:15px;letter-spacing:1px;color:#fff;text-transform:uppercase;white-space:nowrap}
.field{background:#fff;height:27px}
.date-hint{left:828px;top:614px;font-size:8px;font-weight:600;color:#fff;letter-spacing:1px;white-space:nowrap}
.submit{left:703px;top:645px;width:194px;height:32px;font-size:14px}
.body-copy{left:40px;top:733px;width:857px;font-size:11.6px;line-height:16.5px;color:var(--text-muted);letter-spacing:.7px;text-align:justify}
.text-link{left:40px;top:818px;font-family:"Exo 2",sans-serif;font-weight:700;font-size:15px;letter-spacing:1px;color:var(--accent-green);text-transform:uppercase;white-space:nowrap}
.footer{left:40px;top:866px;width:857px;border-top:1px solid #1a1a1a;padding-top:4px;text-align:right;font-size:12.5px;letter-spacing:1px;color:var(--footer-link);white-space:nowrap}
.footer a{color:var(--footer-link);text-decoration:none}
.footer .sep{color:#777;margin:0 6px}
</style>
</head>
<body>
<div class="column">
  <svg class="abs hero" viewBox="0 0 936 384" aria-hidden="true">
    <defs>
      <radialGradient id="glow" cx="0.2" cy="0.35" r="0.5">
        <stop offset="0" stop-color="#1f9a3a"/><stop offset=".5" stop-color="#155a6e"/><stop offset="1" stop-color="#000"/>
      </radialGradient>
      <linearGradient id="swoosh" x1="0" y1="0" x2="1" y2="0">
        <stop offset="0" stop-color="#1e8a1f"/><stop offset=".5" stop-color="#37c13a"/><stop offset="1" stop-color="#1e9a22"/>
      </linearGradient>
    </defs>
    <rect width="936" height="384" fill="#000"/>
    <rect width="700" height="320" fill="url(#glow)"/>
    <path d="M0 255 C180 330 360 330 560 270 C720 222 830 205 936 200 L936 384 L0 384 Z" fill="url(#swoosh)"/>
    <path d="M0 300 C200 360 420 350 600 300 C760 258 860 240 936 236 L936 384 L0 384 Z" fill="#000"/>
    <path d="M0 355 C260 395 520 355 936 318 L936 384 L0 384 Z" fill="#1a7a1c"/>
    <path d="M0 372 C260 410 520 372 936 340 L936 384 L0 384 Z" fill="#000"/>
  </svg>
  <div class="abs hero-photo" role="img" aria-label="Großer schwarzer LCD-Flachbildfernseher auf Standfuß"></div>
  <h1 class="abs headline">
    <span class="small">Mitmachen!</span>
    <span class="l2">Gewinnen!</span>
    <span class="l3">2000.-Sparen!</span>
    <span class="l4">LCD-Sehen!</span>
  </h1>
  <a class="abs pill hero-button">JETZT GEWINNEN</a>

  <h2 class="abs section-title" style="left:40px;top:450px;width:413px"><em>Gewinnen Sie</em> - Diesen tolle LCD Gerat!</h2>
  <div class="abs prize-photo" role="img" aria-label="Kleiner LCD-Fernseher als Preis"></div>
  <p class="abs prize-facts">Unglaubliche 40"<br>16:9 Seitenformat<br>HD Ready<br>2000.- Gesamtwert</p>
  <p class="abs prize-call">Nutzen Sie<br>Ihre Chance!</p>

  <h2 class="abs section-title" style="left:475px;top:450px;width:422px">Sofort mitmachen!</h2>
  <span class="abs form-label" style="top:512px">Vorname:</span>
  <div class="abs field" style="left:613px;top:500px;width:284px"></div>
  <span class="abs form-label" style="top:543px">Nachname:</span>
  <div class="abs field" style="left:613px;top:532px;width:284px"></div>
  <span class="abs form-label" style="top:575px">E-Mail:</span>
  <div class="abs field" style="left:613px;top:564px;width:284px"></div>
  <span class="abs form-label" style="top:610px">Geburtsdatum:</span>
  <div class="abs field" style="left:613px;top:599px;width:50px"></div>
  <div class="abs field" style="left:672px;top:599px;width:51px"></div>
  <div class="abs field" style="left:730px;top:599px;width:89px"></div>
  <span class="abs date-hint">TT &nbsp;MM &nbsp;YYYY</span>
  <a class="abs pill submit">ICH WILL GEWINNEN!</a>

  <h2 class="abs section-title" style="left:40px;top:688px;width:857px">So einfach kann es gehen!</h2>
  <p class="abs body-copy">Das ist ein Mustrtext der durch einen orginalen text ersetyt wir er hat leine Bedeutung dunnd dient nur dem Platz. das ist ein &nbsp;Mustertext Das ist ein Mustrtext der durch einen orginalen text ersetyt wir er hat leine Bedeutung dunnd dient nur dem Platz. das ist ein &nbsp;Das ist ein Mustrtext der durch einen orginalen text ersetyt wir er hat leine Bedeutung dunnd die &nbsp;nt nur dem Platz. das ist ein &nbsp;Mustertext Das ist ein Mustrtext der durch einen orginalen text ersetyt wir er hat leine Bedeutung dunnd dient nur dem Platz. das ist ein</p>
  <a class="abs text-link">&#9658;Jetzt gewinnen</a>
  <nav class="abs footer">
    <a>Startseite</a><span class="sep">|</span><a>Preis</a><span class="sep">|</span><a>Teilnahmebedingungen</a><span class="sep">|</span><a>Datenschutz</a><span class="sep">|</span><a>Impressum</a>
  </nav>
</div>
</body>
</html>
```